Ridge 9 Ridge Turbine Rentals Pty Ltd

We are a hire company based on the Gold Coast in Australia, we Hire out Generators to construction sites, music festivals, parties, fetes etc. Anywhere where power is required we can provide it.

Ridge 9 Ridge Turbine Rentals pty Ltd also provides all leads, distribution boards, Qualified Electricians to perform all connections. we offer refuelling services and mechanical services. 24Hr on call service - to an actual english speaking operator.

Slogan ''Energy Wherever Needed"

Industry/Entity Type

Construction

Contact Information for Business Card

M: 0417285963
E: bookings@ridge9ridgeturbinerentals.com.au

```html
<!DOCTYPE html>
<html lang="en">
<head>
<meta charset="utf-8">
<title>Ridge 9 Ridge Turbine Rentals – Business Card</title>
<link rel="stylesheet" href="https://fonts.googleapis.com/css2?family=Source+Sans+3:wght@400;600;700&display=swap">
<style>
  :root {
    --backdrop: #3b332f;
    --card: #151515;
    --card-edge: #222222;
    --ink-light: #e9e9e9;
    --ink-soft: #c9c9c9;
    --accent: #1f6fa6;
    --accent-light: #7fb8dc;
  }
  * { margin: 0; padding: 0; box-sizing: border-box; }
  html, body {
    width: 1200px; height: 814px; overflow: hidden;
    background: var(--backdrop);
    font-family: "Source Sans 3", "Myriad Pro", Arial, sans-serif;
  }
  .canvas {
    position: relative; width: 1200px; height: 814px;
    display: flex; align-items: center; justify-content: center; gap: 48px;
  }
  .card {
    position: relative; width: 520px; height: 300px;
    background: var(--card);
    border: 1px solid var(--card-edge);
    box-shadow: 0 10px 28px rgba(0,0,0,.45);
    color: var(--ink-light);
  }
  .brand-mark { position: absolute; display: flex; align-items: center; gap: 12px; }
  .brand-mark .brand-square { background: var(--accent-light); }
  .brand-name {
    color: var(--accent-light);
    font-weight: 700; text-transform: uppercase; line-height: 1.05;
  }

  /* front */
  .card--front .brand-mark { top: 44px; right: 44px; }
  .card--front .brand-square { width: 34px; height: 34px; }
  .card--front .brand-name { font-size: 17px; letter-spacing: .5px; }
  .address {
    position: absolute; right: 40px; top: 128px;
    text-align: right; font-size: 15px; line-height: 1.35;
    color: var(--ink-soft); font-style: normal;
  }
  .rule {
    position: absolute; left: 150px; right: 28px; top: 188px;
    height: 1px; background: var(--ink-light);
  }
  .person { position: absolute; left: 26px; top: 172px; }
  .person-name { font-size: 21px; font-weight: 400; color: var(--accent); line-height: 1.1; }
  .person-role { font-size: 15px; color: var(--ink-light); margin-top: 4px; }
  .contacts { position: absolute; left: 26px; top: 234px; list-style: none; font-size: 14px; }
  .contacts li { display: flex; align-items: center; gap: 10px; height: 24px; color: var(--ink-light); }
  .contacts .icon-phone { width: 12px; height: 14px; flex: none; }
  .contacts .icon-mail { width: 14px; height: 12px; flex: none; }

  /* back */
  .card--back .brand-mark {
    top: 56px; left: 0; right: 0;
    flex-direction: column; gap: 14px;
  }
  .card--back .brand-square { width: 64px; height: 64px; }
  .card--back .brand-name { font-size: 24px; text-align: center; letter-spacing: 1px; }
  .slogan {
    position: absolute; left: 0; right: 0; top: 216px;
    text-align: center; font-size: 19px; font-weight: 600; color: var(--ink-light);
  }
</style>
</head>
<body>
<main class="canvas">
  <section class="card card--front" aria-label="Business card front">
    <div class="brand-mark">
      <span class="brand-square"></span>
      <div class="brand-name">Ridge 9 Ridge<br>Turbine Rentals</div>
    </div>
    <address class="address">4210 Banksia Court<br>Burleigh Heads, QLD 4220</address>
    <div class="rule"></div>
    <div class="person">
      <div class="person-name">Liam Carter</div>
      <div class="person-role">CEO/Founder</div>
    </div>
    <ul class="contacts">
      <li>
        <svg class="icon-phone" viewBox="0 0 12 14" aria-hidden="true"><rect x="1" y="0.5" width="10" height="13" rx="1.5" fill="none" stroke="#1f6fa6" stroke-width="1.4"/><rect x="3" y="2.5" width="6" height="7" fill="#1f6fa6"/></svg>
        0417285963
      </li>
      <li>
        <svg class="icon-mail" viewBox="0 0 14 12" aria-hidden="true"><rect x="0" y="1" width="14" height="10" fill="#1f6fa6"/><path d="M0 1 L7 7 L14 1" fill="none" stroke="#151515" stroke-width="1.2"/></svg>
        bookings@ridge9ridgeturbinerentals.com.au
      </li>
    </ul>
  </section>

  <section class="card card--back" aria-label="Business card back">
    <div class="brand-mark">
      <span class="brand-square"></span>
      <div class="brand-name">Ridge 9 Ridge<br>Turbine Rentals</div>
    </div>
    <p class="slogan">Energy Wherever Needed</p>
  </section>
</main>
</body>
</html>
```